IT Services company

we want a modern card design that combines business and technology whilst not being too loud

the Company Name is Corvane Hub and i have attached the logo

can you also put the words Business Enabled Technology under the logo

thanks

Hi can you please show the card with a web url and contact name and email and phone number please

Business

```html
<!DOCTYPE html>
<html lang="en">
<head>
<meta charset="UTF-8">
<title>Corvane Hub — Business Card</title>
<link rel="stylesheet" href="https://fonts.googleapis.com/css2?family=Exo+2:wght@600;700&family=Roboto+Condensed:wght@400&display=swap">
<style>
  :root {
    --backdrop: #3b3b3d;
    --card-frame: #b9c2da;
    --card-face: #ffffff;
    --brand-red: #a8121c;
    --brand-blue: #1f3b93;
    --contact-red: #9c1a20;
  }
  * { margin: 0; padding: 0; box-sizing: border-box; }
  html, body {
    width: 1200px;
    height: 901px;
    overflow: hidden;
    background: var(--backdrop);
  }
  .stage {
    width: 1200px;
    height: 901px;
    display: flex;
    align-items: center;
    justify-content: center;
  }
  .business-card {
    width: 900px;
    height: 540px;
    background: var(--card-frame);
    padding: 26px;
  }
  .card-face {
    position: relative;
    width: 100%;
    height: 100%;
    background: var(--card-face);
    padding: 58px 60px;
  }
  .brand {
    display: flex;
    align-items: center;
    gap: 18px;
  }
  .brand-dot {
    width: 74px;
    height: 74px;
    border-radius: 50%;
    background: var(--brand-red);
    flex: none;
  }
  .brand-name {
    font-family: "Exo 2", sans-serif;
    font-weight: 700;
    font-size: 62px;
    letter-spacing: 1px;
    color: var(--brand-red);
    line-height: 1;
  }
  .tagline {
    margin-top: 14px;
    margin-left: 4px;
    font-family: "Exo 2", sans-serif;
    font-weight: 600;
    font-size: 32px;
    color: var(--brand-blue);
  }
  .contacts {
    position: absolute;
    left: 60px;
    right: 60px;
    bottom: 70px;
    display: flex;
    justify-content: space-between;
    list-style: none;
  }
  .contact-item {
    display: flex;
    align-items: center;
    gap: 12px;
    font-family: "Roboto Condensed", sans-serif;
    font-size: 24px;
    color: var(--contact-red);
  }
  .contact-icon {
    width: 22px;
    height: 22px;
    fill: var(--brand-blue);
    flex: none;
  }
</style>
</head>
<body>
<main class="stage">
  <article class="business-card">
    <div class="card-face">
      <header class="brand">
        <span class="brand-dot"></span>
        <h1 class="brand-name">Corvane Hub</h1>
      </header>
      <p class="tagline">Business Enabled Technology</p>

      <ul class="contacts">
        <li class="contact-item">
          <svg class="contact-icon" viewBox="0 0 24 24" aria-hidden="true">
            <path d="M6.6 10.8a15.1 15.1 0 0 0 6.6 6.6l2.2-2.2a1 1 0 0 1 1-.25 11.4 11.4 0 0 0 3.6.57 1 1 0 0 1 1 1V20a1 1 0 0 1-1 1A17 17 0 0 1 3 4a1 1 0 0 1 1-1h3.5a1 1 0 0 1 1 1c0 1.25.2 2.45.57 3.57a1 1 0 0 1-.25 1z"/>
          </svg>
          <span>(555) 218 4406</span>
        </li>
        <li class="contact-item">
          <svg class="contact-icon" viewBox="0 0 24 24" aria-hidden="true">
            <path d="M2 5h20v14H2z M4 7v.4l8 5.2 8-5.2V7z" fill-rule="evenodd"/>
          </svg>
          <span>mara@corvanehub.com</span>
        </li>
        <li class="contact-item">
          <svg class="contact-icon" viewBox="0 0 24 24" aria-hidden="true">
            <path d="M3 8h8v3H6v2h5v3H3z M21 8h-8v3h5v2h-5v3h8z M8 11h8v2H8z"/>
          </svg>
          <span>www.corvanehub.com</span>
        </li>
      </ul>
    </div>
  </article>
</main>
</body>
</html>
```